Business Card Design for an international medical business

We need a professional and elegant business card design with fashionable graphic element. Our company is located in Hong Kong with three worldwide production lines for medical equipment(surgical face masks, N95, face shields and so on). Our factories all contain medical standard ISOs and all product fulfill Marwick lab and KTR testing standards.

We would like to see designs that show the impression of our professional expertise, formal corporate image with creative thinking work style and inspiring global concept. We want the content in both English and Japanese on the same card. We also want to print our the patent trade mark and company logo on the card.

Target Market(s)

Southeast Asia, US, EU

Industry/Entity Type

Medical Equipment

Contact Information for Business Card

Below are the content we want to be shown on the business card(please help us to simplified them to be more presentable and readable):

Company name: Orlane (Hong Kong) 5K Medical Technology Company Limited
Address: Unit 2204, 22/F, Pebble Tower, No.8 Kendrick Lane, Wan Kei Shan, Hong Kong.
Band Name: Q5K
Homepage: www.quelvane5kbq.example
Name: Lok Wing Sze
Title: Manager
Tel: +852-xxxx-xxxx
Mobile: +852-xxxx-xxxx
Email: xx@orlane5kbq.example

Production Lines:
China: Pei Ling Sun Ke Medical Technology Company Limited
Mo Lan City Rui Fa Textile Machinery Company Limited
Bangladesh: Q5K Medical Technology Company Limited

Qualifications:
ISO 13485:2016
ISO 14644-1:2015
ISO Class 8 Cleanroom
ASTM F2100 Level 2
EN14683 Type IIR
EN149 FFP2
CE Certified
FDA Registration number: XXX

Requirements
Must have
• use pantone color for the design
and provide the pantone number for printing purpose
Should not have
• Background color should not be black.

```html
<!DOCTYPE html>
<html lang="en">
<head>
<meta charset="utf-8">
<title>Quelvane Business Card</title>
<link href="https://fonts.googleapis.com/css2?family=Roboto:wght@400;500;700&display=swap" rel="stylesheet">
<style>
  :root {
    --brand-pink: #e0105a;
    --brand-teal: #1bbbbb;
    --ink: #555a5e;
    --paper: #ffffff;
    --backdrop: #e9e6e2;
  }
  * { margin: 0; padding: 0; box-sizing: border-box; }
  html, body { width: 1200px; height: 1200px; overflow: hidden; }
  body {
    background: var(--backdrop);
    font-family: "Roboto", Arial, sans-serif;
    position: relative;
  }
  .card {
    position: absolute;
    left: 262px;
    width: 686px;
    height: 390px;
    border-radius: 22px;
    overflow: hidden;
    box-shadow: 0 10px 22px rgba(0,0,0,0.18);
  }
  .card-front { top: 166px; background: var(--paper); }
  .card-back { top: 653px; background: var(--brand-teal); color: #fff; }

  .brand {
    position: absolute;
    left: 76px;
    top: 176px;
    display: flex;
    align-items: center;
    gap: 12px;
  }
  .brand-dot {
    width: 16px; height: 16px; border-radius: 50%;
    background: var(--brand-pink);
  }
  .brand-name {
    font-weight: 700;
    font-size: 40px;
    letter-spacing: 0.5px;
    line-height: 1;
    color: var(--brand-pink);
  }
  .divider {
    position: absolute;
    left: 384px; top: 96px;
    width: 1px; height: 199px;
    background: #9a9a9a;
  }
  .contact {
    position: absolute;
    left: 403px; top: 92px;
    color: var(--ink);
  }
  .person-name {
    font-weight: 500;
    font-size: 23px;
    color: var(--brand-pink);
    line-height: 1.2;
  }
  .person-title {
    font-weight: 500;
    font-size: 15.5px;
    color: var(--brand-teal);
    line-height: 1.3;
    margin-bottom: 11px;
  }
  .address { font-size: 15.5px; line-height: 19.5px; margin-bottom: 3px; }
  .contact-list { list-style: none; font-size: 15.5px; line-height: 19.5px; }
  .contact-list li { display: flex; align-items: center; gap: 8px; }
  .contact-list svg { width: 14px; height: 14px; flex: none; fill: var(--brand-pink); }

  .back-info {
    position: absolute;
    right: 46px; top: 44px;
    text-align: right;
    font-size: 15.5px;
    line-height: 19.5px;
  }
  .section-title { font-weight: 700; font-size: 16px; margin-bottom: 9px; }
  .section + .section { margin-top: 48px; }
  .region { font-weight: 500; margin-top: 7px; }
  .region:first-of-type { margin-top: 0; }
</style>
</head>
<body>

<section class="card card-front">
  <div class="brand">
    <span class="brand-dot"></span>
    <span class="brand-name">QUELVANE</span>
  </div>
  <div class="divider"></div>
  <div class="contact">
    <h1 class="person-name">LOK WING SZE</h1>
    <p class="person-title">Manager</p>
    <p class="address">Unit 2204, 22/F, Pebble Tower,<br>No.8 Kendrick Lane,<br>Wan Kei Shan, Hong Kong.</p>
    <ul class="contact-list">
      <li><svg viewBox="0 0 24 24"><path d="M6.6 10.8a15.1 15.1 0 0 0 6.6 6.6l2.2-2.2c.3-.3.7-.4 1-.2 1.1.4 2.3.6 3.6.6.6 0 1 .4 1 1V20c0 .6-.4 1-1 1A17 17 0 0 1 3 4c0-.6.4-1 1-1h3.5c.6 0 1 .4 1 1 0 1.3.2 2.5.6 3.6.1.3 0 .7-.2 1z"/></svg>+852-5310-4472</li>
      <li><svg viewBox="0 0 24 24"><path d="M7 1h10a2 2 0 0 1 2 2v18a2 2 0 0 1-2 2H7a2 2 0 0 1-2-2V3a2 2 0 0 1 2-2zm0 3v14h10V4zm5 15.5a1 1 0 1 0 0 2 1 1 0 0 0 0-2z"/></svg>+852-6038-2915</li>
      <li><svg viewBox="0 0 24 24"><path d="M2 5h20v14H2zm2 2v.5l8 5 8-5V7l-8 5z"/></svg>info@quelvane5kbq.example</li>
      <li><svg viewBox="0 0 24 24"><path d="M12 2a10 10 0 1 0 0 20 10 10 0 0 0 0-20zm-1 17.9A8 8 0 0 1 4.2 10.8L9 15.6v1a2 2 0 0 0 2 2zm6.9-2.5A2 2 0 0 0 16 16h-1v-3a1 1 0 0 0-1-1H8v-2h2a1 1 0 0 0 1-1V7h2a2 2 0 0 0 2-2v-.4a8 8 0 0 1 2.9 12.8z"/></svg>www.quelvane5kbq.example</li>
    </ul>
  </div>
</section>

<section class="card card-back">
  <div class="back-info">
    <div class="section">
      <h2 class="section-title">QUALIFICATIONS</h2>
      <p>ISO 13485:2016 | ISO 14644-1:2015<br>ISO Class 8 Cleanroom | ASTM F2100 Level 2<br>EN14683 Type IIR | EN149 FFP2 | CE Certified</p>
    </div>
    <div class="section">
      <h2 class="section-title">PRODUCTION LINES</h2>
      <p class="region">China:</p>
      <p>Pei Ling Sun Ke<br>Medical Technology Company Limited<br>Mo Lan City Rui Fa<br>Textile Machinery Company Limited</p>
      <p class="region">Bangladesh:</p>
      <p>Q5K Medical Technology Company Limited</p>
    </div>
  </div>
</section>

</body>
</html>
```